Complete Story Outreach Blueprint for digital agencies and web developers and content strategists w

The original design (Complet_Story_Outreach_Blueprint is lacking punch and is too hard to read because items are too small. Please make larger (even if it runs to multiple pages) and add appropriate icons that match the description of the mapping process. This document will be a lead magnet and content upgrade for webinar particpants and opt-ins on webpage.

Target Market(s)

Content marketing strategists, agencies, wordpress developers and entrepreneurs (service providers)

Industry/Entity Type

Digital

Font styles to use
Sans Serif

Colors
85cae6
0293ce
cee9f5

Requirements
Must have
• Title: Complete Story Outreach Blueprint
• url at bottom: www.marnietolliver.com
• Clean design
• Icons that match stage description
Nice to have
• Nice background image that isn't too busy and aligns with the roadmap theme.
• Clear layout like this map:
• https://www.brindlecove.co.uk/the-definitive-guide-to-ecommerce-content-marketing/
• But with a little more sophitication with design.
Should not have
• Cheesy icons that don't match descriptions

```html
<!DOCTYPE html>
<html lang="en">
<head>
<meta charset="utf-8">
<title>Complete Story Outreach Blueprint</title>
<link href="https://fonts.googleapis.com/css2?family=Montserrat:ital,wght@0,600;0,800;1,800&family=Open+Sans:wght@400;600;700&family=PT+Serif:ital,wght@1,700&display=swap" rel="stylesheet">
<style>
:root{
  --bg:#e8eaeb;
  --blue:#0293ce;
  --sky:#85cae6;
  --pale:#cee9f5;
  --navy:#0b4f7c;
  --deep:#0a6ea8;
  --ink:#2b3a46;
  --line:#8d9ba6;
  --white:#ffffff;
}
*{box-sizing:border-box;margin:0;padding:0}
html,body{width:1200px;height:2709px;overflow:hidden;background:var(--bg)}
.board{position:relative;width:664px;height:1500px;transform:scale(1.80723);transform-origin:0 0;font-family:'Open Sans',Arial,sans-serif;color:var(--ink)}
.board>*{position:absolute}
.connectors{left:0;top:0;width:664px;height:1500px}
.lbl{display:block;width:100%;text-align:center}
.title-top{left:0;width:664px;top:38px;text-align:center;font:800 13px/1 'Montserrat',sans-serif;letter-spacing:6px;color:#222}
.title-main{left:0;width:664px;top:58px;text-align:center;font:italic 800 21px/1 'Montserrat',sans-serif;color:#111}
.cue,.question,.step,.chip,.serif-chip,.prompt,.attr,.tool,.draft,.ladder{display:flex;align-items:center;justify-content:center;overflow:hidden}
.cue{background:var(--blue);color:var(--white);border-radius:12px;font:600 9.5px/1.1 'Open Sans',sans-serif}
.question{background:#f7f9fa;border:1px solid var(--sky);border-radius:9px;font:400 6.8px/1.1 'Open Sans',sans-serif;padding:0 3px}
.question b{font-weight:700}
.step{background:var(--white);border:1.3px solid #4ba3d6;border-radius:12px;font:400 10px/1.1 'Open Sans',sans-serif;padding:0 4px 0 12px;color:var(--ink);overflow:visible}
.step b{font-weight:700}
.num{position:absolute;left:-7px;top:-6px;width:16px;height:16px;border-radius:50%;background:var(--navy);border:1.5px solid var(--white);color:var(--white);font:700 6.5px/13px 'Open Sans',sans-serif;text-align:center}
.chip{background:var(--blue);color:var(--white);border-radius:5px;font:400 7px/1.1 'Open Sans',sans-serif;padding:0 3px}
.chip b{font-weight:700}
.serif-chip{background:var(--blue);color:var(--white);border-radius:4px;font:italic 700 6.5px/1 'PT Serif',serif;padding:0 3px}
.prompt{background:var(--white);border:1px solid #9ab7c9;border-radius:3px;font:italic 700 5.9px/1.05 'PT Serif',serif;color:#333;padding:0 2px}
.attr{background:var(--blue);color:var(--white);border-radius:4px;font:italic 700 5.7px/1.05 'PT Serif',serif;padding:0 2px}
.phase-list{list-style:none;font:italic 700 5.9px/1 'PT Serif',serif;color:var(--navy)}
.phase-list li{display:flex;align-items:center;gap:4px;height:12.5px}
.phase-list span{flex:none;width:9px;height:9px;border-radius:50%;border:1px solid var(--navy);font:normal 700 5.5px/7px 'Open Sans',sans-serif;text-align:center}
.tool{background:var(--white);border:1px solid #b6c3cc;border-radius:2px;font:400 5.4px/1.05 'Open Sans',sans-serif}
.art{border-radius:6px;background:linear-gradient(160deg,var(--pale),var(--sky))}
.art.round{border-radius:50%}
.art.navy{background:linear-gradient(160deg,var(--sky),var(--deep))}
.art.light{background:linear-gradient(160deg,#ffffff,#dfe7ec)}
.draft{border-radius:50%;background:var(--blue);color:var(--white);font:600 8px/1.1 'Open Sans',sans-serif}
.ladder{color:var(--white);font:700 7.5px/1.1 'Open Sans',sans-serif;border-radius:10px;padding:0 4px}
.ladder.a{background:var(--blue)}
.ladder.b{background:var(--deep)}
.ladder.c{background:var(--navy)}
.footer{left:0;top:1458px;width:664px;height:42px;background:var(--blue);color:var(--white);font:700 13px/42px 'Montserrat',sans-serif;letter-spacing:2px;text-align:center}
</style>
</head>
<body>
<main class="board">

<svg class="connectors" viewBox="0 0 664 1500" aria-hidden="true">
  <defs>
    <marker id="arrow" viewBox="0 0 6 6" refX="5" refY="3" markerWidth="5" markerHeight="5" orient="auto"><path d="M0 0L6 3L0 6z" fill="#6f7f8b"/></marker>
    <symbol id="yes" viewBox="0 0 16 16"><circle cx="8" cy="8" r="8" fill="#5cb85c"/><path d="M4.2 8.3l2.6 2.6 5-5.3" fill="none" stroke="#fff" stroke-width="2" stroke-linecap="round" stroke-linejoin="round"/></symbol>
    <symbol id="nope" viewBox="0 0 16 16"><circle cx="8" cy="8" r="8" fill="#d9453d"/><path d="M5.2 5.2l5.6 5.6M10.8 5.2l-5.6 5.6" stroke="#fff" stroke-width="2" stroke-linecap="round"/></symbol>
  </defs>
  <g fill="none" stroke="#8d9ba6" stroke-width="1.2">
    <path d="M30 177H545"/>
    <path d="M72 164V177M175 164V177M258 164V177M291 164V177M346 164V177M422 164V177"/>
    <path d="M545 128V143M545 164V172"/>
    <path d="M95 272V292" marker-end="url(#arrow)"/>
    <path d="M160 205H153V330H160M190 332V342"/>
    <path d="M225 267H280" marker-end="url(#arrow)"/>
    <path d="M382 265H411M427 265H432V185H545V182"/>
    <path d="M545 264V290" marker-end="url(#arrow)"/>
    <path d="M165 392H250"/>
    <path d="M266 392H283" marker-end="url(#arrow)"/>
    <path d="M332 278V281"/>
    <path d="M545 370V379"/>
    <path d="M507 385H500V466H507M500 415H440V392H380" marker-end="url(#arrow)"/>
    <path d="M333 402V440H268V406" marker-end="url(#arrow)"/>
    <path d="M333 440H400V406" marker-end="url(#arrow)"/>
    <path d="M263 473V488M281 473V488M398 473V487"/>
    <path d="M263 504V523H240" marker-end="url(#arrow)"/>
    <path d="M281 504V519H294" marker-end="url(#arrow)"/>
    <path d="M398 503V523H418" marker-end="url(#arrow)"/>
    <path d="M190 535V552M213 535V552M323 528V547M343 528V547"/>
    <path d="M190 568V583" marker-end="url(#arrow)"/>
    <path d="M221 560H270V598H286" marker-end="url(#arrow)"/>
    <path d="M250 595H262V640H250"/>
    <path d="M323 563V578" marker-end="url(#arrow)"/>
    <path d="M351 555H372V646" marker-end="url(#arrow)"/>
    <path d="M318 658H298M290 666V681"/>
    <path d="M368 668V682"/>
    <path d="M368 698V711" marker-end="url(#arrow)"/>
    <path d="M390 747H416"/>
    <path d="M424 739V576H470" marker-end="url(#arrow)"/>
    <path d="M376 807V826H354M338 826H248V838" marker-end="url(#arrow)"/>
    <path d="M484 620V639"/>
    <path d="M484 655V671" marker-end="url(#arrow)"/>
    <path d="M532 609H540V639"/>
    <path d="M548 647H572" marker-end="url(#arrow)"/>
    <path d="M594 665V675"/>
    <path d="M594 691V700" marker-end="url(#arrow)"/>
    <path d="M650 781H656V912H593V926" marker-end="url(#arrow)"/>
    <path d="M484 950V972" marker-end="url(#arrow)"/>
    <path d="M593 951V972" marker-end="url(#arrow)"/>
    <path d="M434 1052H402" marker-end="url(#arrow)"/>
    <path d="M545 1084V1108H297" marker-end="url(#arrow)"/>
    <path d="M245 1120V1133H405V1169" marker-end="url(#arrow)"/>
    <path d="M458 1181H513" marker-end="url(#arrow)"/>
    <path d="M405 1232V1249" marker-end="url(#arrow)"/>
    <path d="M405 1272V1330H304" marker-end="url(#arrow)"/>
    <path d="M247 1343V1358" marker-end="url(#arrow)"/>
    <path d="M260 1367H270V1387H246"/>
    <path d="M302 1330H330V1411H348" marker-end="url(#arrow)"/>
    <path d="M457 1411H478" marker-end="url(#arrow)"/>
  </g>
  <g fill="#0293ce">
    <circle cx="72" cy="177" r="2.5"/><circle cx="175" cy="177" r="2.5"/><circle cx="258" cy="177" r="2.5"/><circle cx="291" cy="177" r="2.5"/><circle cx="346" cy="177" r="2.5"/><circle cx="422" cy="177" r="2.5"/>
  </g>
  <circle cx="545" cy="177" r="5" fill="#fff" stroke="#0293ce" stroke-width="1.3"/>
  <use href="#nope" x="411" y="257" width="16" height="16"/>
  <use href="#nope" x="182" y="362" width="16" height="16"/>
  <use href="#yes" x="250" y="384" width="16" height="16"/>
  <use href="#yes" x="324" y="281" width="16" height="16"/>
  <use href="#yes" x="255" y="488" width="16" height="16"/>
  <use href="#nope" x="273" y="488" width="16" height="16"/>
  <use href="#yes" x="390" y="487" width="16" height="16"/>
  <use href="#nope" x="182" y="552" width="16" height="16"/>
  <use href="#yes" x="205" y="552" width="16" height="16"/>
  <use href="#nope" x="315" y="547" width="16" height="16"/>
  <use href="#yes" x="335" y="547" width="16" height="16"/>
  <use href="#nope" x="282" y="650" width="16" height="16"/>
  <use href="#yes" x="360" y="682" width="16" height="16"/>
  <use href="#yes" x="416" y="739" width="16" height="16"/>
  <use href="#nope" x="338" y="818" width="16" height="16"/>
  <use href="#nope" x="476" y="639" width="16" height="16"/>
  <use href="#yes" x="532" y="639" width="16" height="16"/>
  <use href="#yes" x="586" y="675" width="16" height="16"/>
</svg>

<h1 class="title-top">THE COMPLETE STORY</h1>
<p class="title-main">OUTREACH BLUEPRINT FOR AGENCIES &amp; CONSULTANTS</p>

<div class="cue" style="left:484px;top:100px;width:122px;height:28px"><span class="lbl">Answer Questions<br>for Each Phase Below</span></div>

<div class="question" style="left:30px;top:143px;width:95px;height:21px"><span class="lbl">New Topics that <b>Would Appeal at This Stage</b></span></div>
<div class="question" style="left:128px;top:143px;width:97px;height:21px"><span class="lbl">Who are Competitors that <b>Publish Great Content</b></span></div>
<div class="question" style="left:229px;top:143px;width:59px;height:21px"><span class="lbl">Publishing <b>Frequency?</b></span></div>
<div class="question" style="left:290px;top:143px;width:44px;height:21px"><span class="lbl"><b>Format?</b></span></div>
<div class="question" style="left:338px;top:143px;width:68px;height:21px"><span class="lbl">Client <b>Quotes?</b></span></div>
<div class="question" style="left:410px;top:143px;width:68px;height:21px"><span class="lbl">What are they <b>Feeling? Thinking</b></span></div>
<div class="question" style="left:481px;top:143px;width:86px;height:21px"><span class="lbl">Which Phase are We <b>Creating Content For?</b></span></div>

<div class="art navy" style="left:62px;top:205px;width:68px;height:65px" role="img" aria-label="Start banner flag over a chequered finish line"></div>
<div class="art round" style="left:58px;top:298px;width:73px;height:73px" role="img" aria-label="Customer avatar portrait badge"></div>
<div class="step" style="left:30px;top:373px;width:135px;height:32px"><span class="lbl">Do you have <b>an Avatar, Journey &amp; Kw Map?</b></span><span class="num">1</span></div>

<div class="prompt" style="left:160px;top:197px;width:62px;height:13px"><span class="lbl">Engagement Style?</span></div>
<div class="prompt" style="left:160px;top:214px;width:62px;height:13px"><span class="lbl">Solution?</span></div>
<div class="prompt" style="left:160px;top:231px;width:62px;height:13px"><span class="lbl">Pain Points?</span></div>
<div class="prompt" style="left:160px;top:248px;width:62px;height:13px"><span class="lbl">Influencers?</span></div>
<div class="prompt" style="left:160px;top:264px;width:62px;height:17px"><span class="lbl">Hobbies &amp; Interests?</span></div>
<div class="prompt" style="left:160px;top:284px;width:62px;height:13px"><span class="lbl">Demographics?</span></div>
<div class="prompt" style="left:160px;top:301px;width:62px;height:13px"><span class="lbl">Name?</span></div>
<div class="prompt" style="left:160px;top:318px;width:62px;height:13px"><span class="lbl">Gender?</span></div>
<div class="art round light" style="left:180px;top:340px;width:20px;height:20px" role="img" aria-label="Magnifying glass"></div>

<div class="art" style="left:303px;top:187px;width:58px;height:60px" role="img" aria-label="Folded map with location pin"></div>
<div class="step" style="left:283px;top:253px;width:99px;height:24px"><span class="lbl">Journey <b>Mapping</b></span><span class="num">2</span></div>

<div class="art light" style="left:468px;top:190px;width:62px;height:72px" role="img" aria-label="Desktop monitor, tablet and phone"></div>
<ol class="phase-list" style="left:535px;top:200px;width:80px">
  <li><span>1</span>Discover Phase</li>
  <li><span>2</span>Investigation Phase</li>
  <li><span>3</span>Consideration Phase</li>
  <li><span>4</span>Trial Phase</li>
  <li><span>5</span>Purchase Phase</li>
  <li><span>6</span>Promotion Phase</li>
</ol>

<div class="art light" style="left:516px;top:292px;width:52px;height:54px" role="img" aria-label="Keywords document under a magnifying glass"></div>
<div class="step" style="left:496px;top:348px;width:102px;height:23px"><span class="lbl">Keyword <b>Mapping</b></span><span class="num">3</span></div>
<div class="serif-chip" style="left:507px;top:380px;width:73px;height:11px"><span class="lbl">KW Research</span></div>
<div class="serif-chip" style="left:507px;top:393px;width:73px;height:11px"><span class="lbl">Content Topic</span></div>
<div class="serif-chip" style="left:507px;top:406px;width:73px;height:11px"><span class="lbl">SUB Topic</span></div>
<div class="serif-chip" style="left:507px;top:419px;width:73px;height:11px"><span class="lbl">Related Words</span></div>
<div class="serif-chip" style="left:507px;top:432px;width:73px;height:11px"><span class="lbl">Similar Words</span></div>
<div class="serif-chip" style="left:507px;top:445px;width:73px;height:11px"><span class="lbl">Specific Terms</span></div>
<div class="serif-chip" style="left:507px;top:458px;width:73px;height:11px"><span class="lbl">Local Modifiers</span></div>

<div class="art" style="left:295px;top:300px;width:70px;height:78px" role="img" aria-label="Goals checklist clipboard beside a target with an arrow"></div>
<div class="step" style="left:285px;top:380px;width:93px;height:22px"><span class="lbl">Content <b>Goals</b></span><span class="num">4</span></div>

<div class="art light" style="left:256px;top:407px;width:24px;height:41px" role="img" aria-label="Traffic light"></div>
<div class="step" style="left:232px;top:451px;width:80px;height:22px"><span class="lbl">More <b>Traffic</b></span><span class="num">5A</span></div>
<div class="art" style="left:380px;top:405px;width:38px;height:43px" role="img" aria-label="Rising bar chart with trend arrow"></div>
<div class="step" style="left:353px;top:451px;width:91px;height:22px"><span class="lbl">Increased <b>Sales</b></span><span class="num">5B</span></div>

<div class="art light" style="left:183px;top:453px;width:39px;height:55px" role="img" aria-label="Influencer profile clipboard"></div>
<div class="step" style="left:160px;top:512px;width:78px;height:23px"><span class="lbl">Influencer <b>List</b></span><span class="num">6A</span></div>
<div class="art light" style="left:455px;top:453px;width:35px;height:52px" role="img" aria-label="Content page document"></div>
<div class="step" style="left:418px;top:512px;width:102px;height:23px"><span class="lbl">Content <b>Format?</b></span><span class="num">6B</span></div>

<div class="chip" style="left:296px;top:508px;width:68px;height:20px;border-radius:9px"><span class="lbl">Established Relationship</span></div>

<div class="chip" style="left:162px;top:585px;width:88px;height:16px"><span class="lbl">Identify <b>Top Influencers</b></span></div>
<div class="chip" style="left:162px;top:603px;width:88px;height:16px"><span class="lbl">Industry <b>Bloggers</b></span></div>
<div class="chip" style="left:162px;top:621px;width:88px;height:16px"><span class="lbl">Hivemeter/ <b>Pitchstream</b></span></div>
<div class="chip" style="left:162px;top:639px;width:88px;height:16px"><span class="lbl"><b>Trendpulse</b></span></div>

<div class="tool" style="left:288px;top:580px;width:78px;height:11px"><span class="lbl">Subscribe to Email list</span></div>
<div class="tool" style="left:288px;top:593px;width:78px;height:11px"><span class="lbl">Add Blog to Feedhaven</span></div>
<div class="tool" style="left:288px;top:606px;width:78px;height:18px"><span class="lbl">Like &amp; Comment on<br>Social Media/Blogs</span></div>
<div class="tool" style="left:288px;top:626px;width:78px;height:11px"><span class="lbl">Reachout</span></div>

<div class="chip" style="left:318px;top:648px;width:82px;height:20px;border-radius:9px"><span class="lbl">Identify Trending<br>Industry Content</span></div>
<div class="tool" style="left:278px;top:683px;width:29px;height:15px"><span class="lbl">Rankly</span></div>
<div class="tool" style="left:262px;top:701px;width:31px;height:15px"><span class="lbl">Linkscope</span></div>
<div class="tool" style="left:252px;top:720px;width:33px;height:15px"><span class="lbl">Trendpulse</span></div>
<div class="tool" style="left:243px;top:739px;width:30px;height:15px"><span class="lbl">Midpage</span></div>
<div class="tool" style="left:231px;top:758px;width:30px;height:17px"><span class="lbl">Topic<br>Jewels</span></div>

<div class="art light" style="left:345px;top:713px;width:43px;height:57px" role="img" aria-label="Decided format clipboard"></div>
<div class="step" style="left:340px;top:785px;width:74px;height:22px"><span class="lbl">Decided <b>Format?</b></span><span class="num">7A</span></div>

<div class="chip" style="left:163px;top:843px;width:88px;height:12px"><span class="lbl"><b>Infographics</b></span></div>
<div class="chip" style="left:253px;top:843px;width:83px;height:12px"><span class="lbl"><b>Video</b></span></div>
<div class="chip" style="left:161px;top:857px;width:88px;height:12px"><span class="lbl">Metric <b>Chart</b></span></div>
<div class="chip" style="left:251px;top:857px;width:83px;height:12px"><span class="lbl">Press <b>Release</b></span></div>
<div class="chip" style="left:159px;top:871px;width:88px;height:12px"><span class="lbl"><b>Listicle</b></span></div>
<div class="chip" style="left:249px;top:871px;width:83px;height:12px"><span class="lbl"><b>Tweets</b></span></div>
<div class="chip" style="left:157px;top:884px;width:88px;height:12px"><span class="lbl">Guest <b>Posts</b></span></div>
<div class="chip" style="left:247px;top:884px;width:83px;height:12px"><span class="lbl"><b>Webinar</b></span></div>
<div class="chip" style="left:155px;top:898px;width:88px;height:12px"><span class="lbl"><b>Article</b></span></div>
<div class="chip" style="left:245px;top:898px;width:83px;height:12px"><span class="lbl"><b>White</b> Paper</span></div>
<div class="chip" style="left:153px;top:911px;width:88px;height:12px"><span class="lbl"><b>eBook</b></span></div>
<div class="chip" style="left:243px;top:911px;width:83px;height:12px"><span class="lbl">Ultimate <b>Guide</b></span></div>
<div class="chip" style="left:151px;top:925px;width:88px;height:12px"><span class="lbl">Case <b>Study</b></span></div>
<div class="chip" style="left:241px;top:925px;width:83px;height:12px"><span class="lbl">Expert <b>Round Up</b></span></div>
<div class="chip" style="left:149px;top:939px;width:88px;height:12px"><span class="lbl"><b>FAQ</b></span></div>
<div class="chip" style="left:239px;top:939px;width:83px;height:12px"><span class="lbl"><b>Testimonials</b></span></div>
<div class="chip" style="left:147px;top:952px;width:88px;height:12px"><span class="lbl">Worknet <b>Posts</b></span></div>
<div class="chip" style="left:237px;top:952px;width:83px;height:12px"><span class="lbl">Client <b>Showcase</b></span></div>
<div class="chip" style="left:145px;top:966px;width:88px;height:12px"><span class="lbl"><b>News</b></span></div>
<div class="chip" style="left:235px;top:966px;width:83px;height:12px"><span class="lbl"><b>Deckshare</b></span></div>

<div class="art light" style="left:477px;top:550px;width:48px;height:48px" role="img" aria-label="Desk calendar page"></div>
<div class="step" style="left:437px;top:598px;width:98px;height:22px"><span class="lbl">Editorial <b>Calendar?</b></span><span class="num">8</span></div>
<div class="attr" style="left:441px;top:673px;width:85px;height:11px"><span class="lbl">List of Topic Pitches</span></div>
<div class="attr" style="left:441px;top:687px;width:85px;height:11px"><span class="lbl">National Awareness Days</span></div>
<div class="attr" style="left:441px;top:701px;width:85px;height:11px"><span class="lbl">Industry News &amp; Event</span></div>
<div class="attr" style="left:441px;top:715px;width:85px;height:11px"><span class="lbl">Industry Magazine Editorials</span></div>
<div class="attr" style="left:441px;top:729px;width:85px;height:11px"><span class="lbl">Promotional Campaigns</span></div>
<div class="attr" style="left:441px;top:743px;width:85px;height:11px"><span class="lbl">Brain Storm Headlines</span></div>
<div class="attr" style="left:441px;top:757px;width:85px;height:11px"><span class="lbl">Create Topic Outline</span></div>
<div class="attr" style="left:441px;top:771px;width:85px;height:11px"><span class="lbl">Choose Format</span></div>
<div class="attr" style="left:441px;top:785px;width:85px;height:11px"><span class="lbl">Images</span></div>
<div class="attr" style="left:441px;top:799px;width:85px;height:11px"><span class="lbl">Publication Date</span></div>
<div class="attr" style="left:441px;top:813px;width:85px;height:11px"><span class="lbl">Assign Writer</span></div>
<div class="attr" style="left:441px;top:827px;width:85px;height:16px"><span class="lbl">Decide On Content<br>Promo Channels</span></div>
<div class="attr" style="left:441px;top:846px;width:85px;height:11px"><span class="lbl">Paid Promotion Strategy</span></div>

<div class="draft" style="left:572px;top:623px;width:44px;height:44px"><span class="lbl">1st Draft<br>Created?</span></div>
<div class="art light" style="left:565px;top:702px;width:47px;height:63px" role="img" aria-label="Quality control checklist clipboard"></div>
<div class="step" style="left:558px;top:768px;width:92px;height:28px"><span class="lbl">Quality <b>Control<br>Checklist</b></span><span class="num">9</span></div>
<div class="prompt" style="left:555px;top:806px;width:85px;height:12px"><span class="lbl">Catchy Headline?</span></div>
<div class="prompt" style="left:555px;top:820px;width:85px;height:12px"><span class="lbl">Appealing Images?</span></div>

<div class="art" style="left:462px;top:862px;width:68px;height:48px" role="img" aria-label="Megaphone"></div>
<div class="step" style="left:432px;top:927px;width:105px;height:23px"><span class="lbl">Organic <b>Promotion</b></span><span class="num">10</span></div>
<div class="cue" style="left:571px;top:928px;width:44px;height:23px;font-weight:700"><span class="lbl">SEO</span></div>

<div class="chip" style="left:434px;top:975px;width:106px;height:20px"><span class="lbl"><b>Image Alt Tags Optimized</b></span></div>
<div class="chip" style="left:434px;top:997px;width:106px;height:23px"><span class="lbl"><b>Target Keyword In Title/Body and H1, H2, H3</b></span></div>
<div class="chip" style="left:434px;top:1023px;width:106px;height:18px"><span class="lbl"><b>Keyword In URL</b></span></div>
<div class="chip" style="left:434px;top:1044px;width:106px;height:18px"><span class="lbl"><b>Optimized MetaData</b></span></div>
<div class="chip" style="left:434px;top:1065px;width:106px;height:19px"><span class="lbl"><b>Mobile Friendly</b></span></div>
<div class="chip" style="left:543px;top:975px;width:109px;height:23px"><span class="lbl"><b>Internal Linking Strategy To Relevant Posts</b></span></div>
<div class="chip" style="left:543px;top:1000px;width:109px;height:23px"><span class="lbl"><b>Authority Link In 1st Paragraph</b></span></div>
<div class="chip" style="left:543px;top:1026px;width:109px;height:20px"><span class="lbl"><b>Social Share Enabled</b></span></div>
<div class="chip" style="left:543px;top:1050px;width:109px;height:24px"><span class="lbl"><b>Embed Infuencer Links In Content</b></span></div>

<div class="art light" style="left:318px;top:985px;width:60px;height:52px" role="img" aria-label="Monitor with bar chart and settings gear"></div>
<div class="step" style="left:296px;top:1039px;width:106px;height:27px"><span class="lbl">Outreach<br><b>Optimization</b></span><span class="num">11</span></div>

<div class="art" style="left:211px;top:1037px;width:60px;height:53px" role="img" aria-label="Video player with padlock and music note"></div>
<div class="step" style="left:190px;top:1094px;width:105px;height:27px"><span class="lbl">Content<br><b>Promotion</b></span><span class="num">12</span></div>

<div class="ladder a" style="left:22px;top:1138px;width:108px;height:18px"><span class="lbl">Get Approval</span></div>
<div class="ladder a" style="left:132px;top:1149px;width:108px;height:18px"><span class="lbl">Make Revisions</span></div>
<div class="ladder a" style="left:242px;top:1160px;width:108px;height:18px"><span class="lbl">Request Approval</span></div>
<div class="ladder a" style="left:350px;top:1171px;width:108px;height:19px"><span class="lbl">Notify Influencer List</span></div>
<div class="ladder c" style="left:22px;top:1178px;width:108px;height:19px"><span class="lbl">Vidstream</span></div>
<div class="ladder b" style="left:132px;top:1188px;width:108px;height:20px"><span class="lbl">Circlebook</span></div>
<div class="ladder c" style="left:242px;top:1199px;width:108px;height:21px"><span class="lbl">Worknet</span></div>
<div class="ladder a" style="left:350px;top:1209px;width:108px;height:23px"><span class="lbl">Create &amp; Publish Social Media Teaser Verbiage</span></div>
<div class="ladder a" style="left:352px;top:1251px;width:108px;height:21px"><span class="lbl">Email Subscriber<br>List</span></div>

<div class="art round navy" style="left:546px;top:1155px;width:42px;height:42px" role="img" aria-label="Share icon badge"></div>
<div class="step" style="left:515px;top:1205px;width:105px;height:28px"><span class="lbl"><b>Publish</b><br><b>Content to CMS</b></span><span class="num">13</span></div>

<div class="art" style="left:214px;top:1256px;width:68px;height:52px" role="img" aria-label="Ads billboard"></div>
<div class="step" style="left:193px;top:1316px;width:109px;height:27px"><span class="lbl">Paid<br><b>Advertising?</b></span><span class="num">14</span></div>
<div class="chip" style="left:235px;top:1359px;width:25px;height:15px"><span class="lbl"><b>PPC</b></span></div>
<div class="chip" style="left:223px;top:1380px;width:23px;height:15px"><span class="lbl"><b>CB</b></span></div>

<div class="art light" style="left:370px;top:1352px;width:70px;height:43px" role="img" aria-label="Analytics dashboard monitor with magnifier"></div>
<div class="step" style="left:350px;top:1397px;width:107px;height:28px"><span class="lbl">Measure/<br><b>Analytics</b></span><span class="num">15</span></div>
<div class="art round" style="left:510px;top:1350px;width:45px;height:43px" role="img" aria-label="Circular repurpose target"></div>
<div class="step" style="left:480px;top:1398px;width:107px;height:27px"><span class="lbl">Repurpose<br><b>Content</b></span><span class="num">16</span></div>

<footer class="footer">www.marnietolliver.com</footer>
</main>
</body>
</html>
```